Consulting company needs website design

We need a simple, static website design for our consulting company. We are looking for a general design of the look and feel of the website. Initially, it will have these pages:
- Home
- About us
- Services
- Contact us
We have our own logo which I have attached to the brief.

We are looking for a simple website, with white background and the use of gray (darker) as the main theme. Simple fonts. The website should be responsive so it an be easily red in mobile devices.

As part of the project, we will need to receive at least the following items:
- Individual files with sample text to support the pages outlined above
- Necessary CSS files

Our current website is here: http://www.lantrovale.co/

Here are some examples of other website we like to be used as guideline:
- http://www.morvicaplanos.com/
-

Target Market(s)

Individuals and companies looking to hire our company to provide consulting services.

Industry/Entity Type

It Company

Coding

Coded - Design and coding required

Number of Pages Required

4 page

Font styles to use
Sans Serif

Requirements
Must have
• Main page should have the ability to embed Chirplet feed into it.
• We prefer the design to use gray tones.

```html
<!DOCTYPE html>
<html lang="en">
<head>
<meta charset="utf-8">
<title>Lantrovale Group SAS</title>
<link href="https://fonts.googleapis.com/css2?family=Open+Sans:wght@400;600;700&family=Arimo:wght@400;700&display=swap" rel="stylesheet">
<style>
:root{
  --ink:#4a4a4a;
  --muted:#8a8a8a;
  --nav:#353535;
  --nav-active:#cfcfcf;
  --band:#dedede;
  --band-dark:#5a5a5a;
  --footer:#5f5f5f;
  --white:#ffffff;
  --link:#1da1e6;
}
*{box-sizing:border-box;margin:0;padding:0}
html,body{width:1200px;height:2344px;overflow:hidden;background:var(--white)}
body{position:relative;font-family:"Arimo",Arial,sans-serif;color:var(--ink)}
.abs{position:absolute}
.heading{font-family:"Open Sans",Arial,sans-serif}

/* hero */
.hero{left:0;top:0;width:1200px;height:614px;background:linear-gradient(160deg,#6f7276 0%,#54575c 45%,#3f4246 100%)}
.hero-call{right:80px;top:32px;color:var(--white);display:flex;align-items:center;gap:14px}
.hero-call small{display:block;font-family:"Open Sans",sans-serif;font-size:17px;opacity:.85}
.hero-call strong{display:block;font-family:"Open Sans",sans-serif;font-size:33px;font-weight:600;line-height:1}
.brand{left:352px;top:248px;display:flex;align-items:center;gap:30px}
.brand-dot{width:180px;height:180px;border-radius:50%;background:rgba(255,255,255,.85)}
.brand-name{font-family:"Open Sans",sans-serif;font-size:56px;line-height:1.35;color:var(--white);font-weight:400}

/* nav */
.nav{left:0;top:614px;width:1200px;height:63px;background:var(--nav)}
.nav ul{list-style:none;display:flex;position:absolute;left:288px;top:0;height:63px}
.nav li{font-family:"Arimo",sans-serif;font-size:17px;color:#e8e8e8;height:63px;line-height:63px;padding:0 40px}
.nav li.active{background:var(--nav-active);color:#333;width:125px;padding:0;text-align:center}

/* welcome */
.welcome-title{left:0;width:1200px;top:730px;text-align:center;font-size:43px;color:#555}
.welcome-text{left:140px;width:920px;top:795px;text-align:center;font-size:14.5px;line-height:27px;color:var(--muted)}

/* services */
.service{top:938px;width:333px;text-align:center}
.service-photo{margin-top:37px;width:333px;height:188px}
.service-hex{position:absolute;left:128px;top:0}
.service-title{margin-top:35px;font-family:"Open Sans",sans-serif;font-size:21px;color:#444}
.service-text{margin:12px auto 0;width:300px;font-size:15px;line-height:25px;color:var(--muted)}
.more{display:inline-block;margin-top:16px;width:114px;height:51px;line-height:49px;border:1.5px solid #9a9a9a;font-family:"Open Sans",sans-serif;font-size:18px;color:#555}

/* tweets */
.tweets{left:78px;top:1403px;width:1044px;height:147px;background:var(--band);border:1px solid #c9c9c9}
.tweets-label{left:0;top:0;height:145px}
.tweets-label span{position:absolute;left:0;top:30px;width:210px;text-align:center;font-family:"Open Sans",sans-serif;font-size:32px;line-height:38px;color:var(--white)}
.tweet-dot{left:245px;top:53px;width:40px;height:40px;border-radius:50%;background:var(--link)}
.tweet{left:307px;top:34px;width:720px;font-size:15px;line-height:23px;color:#444}
.tweet b{font-family:"Open Sans",sans-serif;font-weight:700;color:#333;font-size:16px}
.tweet .handle{color:#555}
.tweet a{color:var(--link);text-decoration:none}
.tweet-date{right:22px;top:44px;font-size:13px;color:#555}
.pager{right:18px;top:112px;display:flex;gap:8px;align-items:center}
.pager i{display:block;width:7px;height:7px;border-radius:50%;background:#555}
.pager i.on{width:15px;height:15px;background:none;border:2px solid #555;position:relative}
.pager i.on::after{content:"";position:absolute;left:2.5px;top:2.5px;width:6px;height:6px;border-radius:50%;background:#555}

/* news */
.news-title{left:0;width:1200px;top:1603px;text-align:center;font-size:43px;color:#555}
.news{top:1672px;width:250px}
.news-photo{width:250px;height:156px}
.news-date{margin-top:24px;padding-left:3px;font-family:"Open Sans",sans-serif;font-size:16.5px;color:#444}
.news-text{margin-top:9px;padding-left:3px;font-size:15px;line-height:25px;color:var(--muted)}
.read{margin-top:10px;padding-left:3px;font-family:"Open Sans",sans-serif;font-weight:700;font-size:15px;color:#444}

/* footer */
.footer{left:0;top:2041px;width:1200px;height:303px;background:var(--footer);color:var(--white)}
.f-head{font-family:"Open Sans",sans-serif;font-size:20px;color:var(--white);position:absolute;top:30px}
.f-links{position:absolute;left:81px;top:72px;list-style:none;font-size:14.5px;line-height:27px;color:#eee}
.f-links li::before{content:"»";margin-right:12px}
.f-contact{position:absolute;left:345px;top:72px;font-size:14.5px;line-height:27px;color:#eee}
.f-row{display:flex;gap:14px;align-items:flex-start;margin-bottom:8px}
.f-row svg{flex:none;margin-top:5px}
.f-news-text{position:absolute;left:610px;top:70px;font-size:14px;color:#eee}
.f-input{position:absolute;left:607px;top:104px;width:250px;height:51px;border:1.5px solid #eee;font-size:15px;line-height:48px;padding-left:14px}
.f-btn{position:absolute;left:607px;top:157px;width:146px;height:53px;background:var(--white);color:#333;font-family:"Open Sans",sans-serif;font-weight:700;font-size:18px;line-height:53px;text-align:center}
.f-brand{position:absolute;left:905px;top:45px;width:170px;text-align:center;font-family:"Open Sans",sans-serif;font-size:26px;line-height:32px;color:var(--white)}
.f-rule{position:absolute;left:920px;top:150px;width:158px;height:1px;background:#888}
.f-social{position:absolute;left:937px;top:172px;display:flex;gap:9px}
.f-social i{display:block;width:34px;height:34px;border-radius:50%;border:1.5px solid #fff}
.f-social i:first-child{background:#fff}
.f-bottom{position:absolute;left:78px;top:240px;width:1044px;height:1px;background:#777}
.f-copy{position:absolute;left:0;width:1200px;top:265px;text-align:center;font-size:14px;color:#ddd}
.f-copy b{font-weight:400;color:#fff;font-size:15px}
</style>
</head>
<body>

<header>
  <div class="abs hero" role="img" aria-label="Photo from above of business people in suits seated in a circle of office chairs, under a grey overlay"></div>
  <div class="abs hero-call">
    <svg width="40" height="44" viewBox="0 0 24 24" aria-hidden="true"><path fill="#fff" d="M6.6 10.8c1.4 2.8 3.8 5.1 6.6 6.6l2.2-2.2c.3-.3.7-.4 1-.2 1.1.4 2.3.6 3.6.6.6 0 1 .4 1 1V20c0 .6-.4 1-1 1C10.6 21 3 13.4 3 4c0-.6.4-1 1-1h3.5c.6 0 1 .4 1 1 0 1.3.2 2.5.6 3.6.1.3 0 .7-.2 1z"/></svg>
    <div><small>Call Us Know</small><strong>123 456 7890</strong></div>
  </div>
  <div class="abs brand">
    <div class="brand-dot"></div>
    <div class="brand-name">Lantrovale<br>Group SAS</div>
  </div>
  <nav class="abs nav">
    <ul>
      <li class="active">HOME</li>
      <li>ABOUT US</li>
      <li>SERVICES</li>
      <li>CONTACT US</li>
    </ul>
  </nav>
</header>

<main>
  <h1 class="abs heading welcome-title" style="font-weight:400">Welcome To Lantrovale Group Sas</h1>
  <p class="abs welcome-text">Lorem Ipsum is simply dummy text of the printing and typesetting industry. Lorem Ipsum has been the industry's standard dummy text ever since the 1500s, when an unknown printer took a galley of type and scrambled it to make a type specimen book. It has survived not only five centuries, but also the leap into electronic typesetting, remaining essentially unchanged. It was popularised in the 1960s with the release of Letraset sheets containing Lorem Ipsum passages</p>

  <section class="abs service" style="left:78px">
    <div class="service-photo" role="img" aria-label="Photo of a consultant presenting at a flip chart to seated colleagues" style="background:linear-gradient(135deg,#e9eaec,#b9bcc1 60%,#6e7277)"></div>
    <svg class="service-hex" width="76" height="76" viewBox="0 0 76 76" aria-hidden="true"><polygon points="38,2 68,17 72,50 52,74 24,74 4,50 8,17" fill="#5a5a5a"/><circle cx="38" cy="38" r="11" fill="none" stroke="#fff" stroke-width="3"/></svg>
    <h2 class="service-title" style="font-weight:400">BUSINESS STRATEGY</h2>
    <p class="service-text">Lorem Ipsum is simply dummy text of the printing and typesetting .</p>
    <span class="more">MORE</span>
  </section>

  <section class="abs service" style="left:433px">
    <div class="service-photo" role="img" aria-label="Photo of a businessman holding a tablet with floating charts and a world map" style="background:linear-gradient(135deg,#3b3d42,#c9cacd 55%,#efefef)"></div>
    <svg class="service-hex" width="76" height="76" viewBox="0 0 76 76" aria-hidden="true"><polygon points="38,2 68,17 72,50 52,74 24,74 4,50 8,17" fill="#5a5a5a"/><circle cx="38" cy="38" r="11" fill="none" stroke="#fff" stroke-width="3"/></svg>
    <h2 class="service-title" style="font-weight:400">MANAGEMENT</h2>
    <p class="service-text">Lorem Ipsum is simply dummy text of the printing and typesetting .</p>
    <span class="more">MORE</span>
  </section>

  <section class="abs service" style="left:789px">
    <div class="service-photo" role="img" aria-label="Photo of colleagues gathered around a laptop in a coaching session" style="background:linear-gradient(135deg,#4a4c50,#8d8f93 50%,#d9d9da)"></div>
    <svg class="service-hex" width="76" height="76" viewBox="0 0 76 76" aria-hidden="true"><polygon points="38,2 68,17 72,50 52,74 24,74 4,50 8,17" fill="#5a5a5a"/><circle cx="38" cy="38" r="11" fill="none" stroke="#fff" stroke-width="3"/></svg>
    <h2 class="service-title" style="font-weight:400">EXECUTIVE COACHING</h2>
    <p class="service-text">Lorem Ipsum is simply dummy text of the printing and typesetting .</p>
    <span class="more">MORE</span>
  </section>

  <section class="abs tweets">
    <svg class="abs tweets-label" width="218" height="145" viewBox="0 0 218 145" aria-hidden="true"><polygon points="0,0 190,0 218,72.5 190,145 0,145" fill="var(--band-dark)"/></svg>
    <div class="abs tweets-label"><span>OUR<br>TWEETS</span></div>
    <div class="abs tweet-dot"></div>
    <div class="abs tweet-date">Jul 14</div>
    <p class="abs tweet"><b>Lantrovale Group</b> <span class="handle">@Lantrovale Group</span><br>Great insights about <a>#data</a> and <a>#analytics</a> at the Northbay CDO/Information Quality Symposium http://lnk.ex/4kq2pa<br><a>http://lnk.ex/7tr9wm</a></p>
    <div class="abs pager"><i></i><i class="on"></i><i></i></div>
  </section>

  <h2 class="abs heading news-title" style="font-weight:400">Latest News</h2>

  <article class="abs news" style="left:78px">
    <div class="news-photo" role="img" aria-label="Photo of a businessman touching a glowing digital interface" style="background:linear-gradient(135deg,#1d3347,#3f6684 55%,#a9c1d3)"></div>
    <div class="news-date">18 July, 2016</div>
    <p class="news-text">Lorem Ipsum is simply dummy text of the printing and type setting the industry &nbsp;standard...</p>
    <div class="read">READ MORE... »</div>
  </article>
  <article class="abs news" style="left:344px">
    <div class="news-photo" role="img" aria-label="Photo of smiling colleagues meeting at an office table" style="background:linear-gradient(135deg,#f1f1f1,#b6b8bb 55%,#55585c)"></div>
    <div class="news-date">18 July, 2016</div>
    <p class="news-text">Lorem Ipsum is simply dummy text of the printing and type setting the industry &nbsp;standard...</p>
    <div class="read">READ MORE... »</div>
  </article>
  <article class="abs news" style="left:608px">
    <div class="news-photo" role="img" aria-label="Photo from above of a team around a white conference table" style="background:linear-gradient(135deg,#dfe3e6,#a3a9ae 55%,#6a6f75)"></div>
    <div class="news-date">18 July, 2016</div>
    <p class="news-text">Lorem Ipsum is simply dummy text of the printing and type setting the industry &nbsp;standard...</p>
    <div class="read">READ MORE... »</div>
  </article>
  <article class="abs news" style="left:873px">
    <div class="news-photo" role="img" aria-label="Photo of hands reviewing financial charts beside glasses on a desk" style="background:linear-gradient(135deg,#6f8aa3,#b4c5d4 55%,#e7edf2)"></div>
    <div class="news-date">18 July, 2016</div>
    <p class="news-text">Lorem Ipsum is simply dummy text of the printing and type setting the industry &nbsp;standard...</p>
    <div class="read">READ MORE... »</div>
  </article>
</main>

<footer class="abs footer">
  <h3 class="f-head" style="left:81px;font-weight:400">USEFUL LINKS</h3>
  <ul class="f-links">
    <li style="color:#fff">Home</li>
    <li>About Us</li>
    <li>Service</li>
    <li>Contact Us</li>
  </ul>

  <h3 class="f-head" style="left:345px;font-weight:400">CONTACT INFO</h3>
  <div class="f-contact">
    <div class="f-row">
      <svg width="16" height="20" viewBox="0 0 16 20" aria-hidden="true"><path fill="#fff" d="M8 0a7 7 0 0 0-7 7c0 5 7 13 7 13s7-8 7-13a7 7 0 0 0-7-7zm0 9.5A2.5 2.5 0 1 1 8 4.5a2.5 2.5 0 0 1 0 5z"/></svg>
      <span>123 Building Name, Street,<br>City, Country - Zip code</span>
    </div>
    <div class="f-row">
      <svg width="16" height="16" viewBox="0 0 24 24" aria-hidden="true"><path fill="#fff" d="M6.6 10.8c1.4 2.8 3.8 5.1 6.6 6.6l2.2-2.2c.3-.3.7-.4 1-.2 1.1.4 2.3.6 3.6.6.6 0 1 .4 1 1V20c0 .6-.4 1-1 1C10.6 21 3 13.4 3 4c0-.6.4-1 1-1h3.5c.6 0 1 .4 1 1 0 1.3.2 2.5.6 3.6.1.3 0 .7-.2 1z"/></svg>
      <span>01 2345 6789</span>
    </div>
    <div class="f-row">
      <svg width="18" height="14" viewBox="0 0 18 14" aria-hidden="true"><rect x="0" y="0" width="18" height="14" rx="2" fill="#fff"/><path d="M1 2l8 6 8-6" fill="none" stroke="#5f5f5f" stroke-width="1.6"/></svg>
      <span>Info@lantrovale.co</span>
    </div>
  </div>

  <h3 class="f-head" style="left:620px;font-weight:400">NEWSLETTER</h3>
  <p class="f-news-text">Subscribe to stay on Lantrovale Group</p>
  <div class="f-input">Enter Email Id</div>
  <div class="f-btn">SUBSCRIBE</div>

  <div class="f-brand">Lantrovale<br>Group</div>
  <div class="f-rule"></div>
  <div class="f-social" aria-hidden="true"><i></i><i></i><i></i></div>

  <div class="f-bottom"></div>
  <p class="f-copy">©<b>Lantrovale Group</b> - 2016. All Rights Reserved.</p>
</footer>

</body>
</html>
```